2nd Generation Blind Manufacturer & Retailer Needs A Stationary Set

We need a stationary set for a family business located the in the Whitsundays (QLD). We retail and manufacture blinds awnings and shutters. Second generation, in operation for over 30 years.

Final draft must include at minimum:

Business Card (2 Sided)
Letterhead
Presentation Folder

Target Market(s)

home owners, landlords, builders, real estate agents, shopping centres

Industry/Entity Type

Textile

Requirements
Must have
• Design needs to work in mono as well as colour print
Nice to have
• Relevant to the textile industry
Should not have
• The inclusion of blinds, awnings or shutters is an automatic no-no

```html
<!DOCTYPE html>
<html lang="en">
<head>
<meta charset="utf-8">
<title>Kestrel Blinds — Stationery Set</title>
<link href="https://fonts.googleapis.com/css2?family=Cinzel:wght@400;500&family=Pinyon+Script&display=swap" rel="stylesheet">
<style>
  :root {
    --backdrop: #e8e8e8;
    --paper: #f4f4f4;
    --paper-white: #fafafa;
    --brand-grey: #6d6d6d;
    --mark-grey: #858585;
    --ink: #6a6a6a;
    --accent: #1fb3ad;
  }
  * { margin: 0; padding: 0; box-sizing: border-box; }
  html, body { width: 1200px; height: 1000px; overflow: hidden; }
  body {
    background: var(--backdrop);
    font-family: "Cinzel", Georgia, serif;
    color: var(--ink);
    position: relative;
  }
  .piece { position: absolute; background: var(--paper); overflow: hidden; box-shadow: 0 2px 6px rgba(0,0,0,0.12); }
  .band { position: absolute; left: 0; right: 0; bottom: 0; background: var(--brand-grey); }

  .brand { position: absolute; display: flex; align-items: center; gap: 8px; }
  .brand-square { background: var(--accent); flex: none; }
  .brand-name {
    font-family: "Cinzel", Georgia, serif;
    font-weight: 500; color: var(--ink); text-transform: uppercase;
    letter-spacing: 0.02em; line-height: 1;
  }

  /* envelope back */
  .envelope-back { left: 55px; top: 145px; width: 341px; height: 170px; }
  .envelope-back svg { position: absolute; left: 0; top: 0; }
  .flap-square { position: absolute; left: 156px; top: 9px; width: 28px; height: 28px; background: var(--paper-white); }

  /* envelope front */
  .envelope-front { left: 57px; top: 382px; width: 340px; height: 170px; }
  .envelope-front .band { height: 30px; }

  /* compliments slip */
  .compliments { left: 58px; top: 625px; width: 310px; height: 154px; }
  .compliments .band { height: 27px; }
  .compliments-note {
    position: absolute; right: 12px; bottom: 31px;
    font-family: "Pinyon Script", cursive; font-size: 14px; color: var(--ink);
  }

  /* letterhead */
  .letterhead { left: 430px; top: 143px; width: 325px; height: 460px; }
  .letterhead .band { height: 30px; }

  /* folder */
  .folder { left: 800px; top: 143px; width: 357px; height: 488px; }
  .folder .band { height: 260px; }
  .folder-square { position: absolute; left: 132px; top: 314px; width: 90px; height: 91px; background: var(--mark-grey); }

  /* cd */
  .cd-disc { position: absolute; left: 522px; top: 627px; filter: drop-shadow(0 2px 4px rgba(0,0,0,0.12)); }
  .cd-sleeve { left: 429px; top: 628px; width: 195px; height: 194px; background: var(--paper-white); }
  .cd-sleeve .band { height: 98px; }
  .sleeve-square { position: absolute; left: 78px; top: 124px; width: 38px; height: 40px; background: var(--mark-grey); }

  /* business cards */
  .card-back { left: 799px; top: 675px; width: 140px; height: 69px; background: var(--brand-grey); }
  .card-back-square { position: absolute; left: 59px; top: 18px; width: 22px; height: 22px; background: var(--mark-grey); }
  .card-back-url {
    position: absolute; left: 0; right: 0; top: 56px; text-align: center;
    font-size: 4px; letter-spacing: 0.08em; color: #8c8c8c; text-transform: uppercase;
  }
  .card-front { left: 1017px; top: 671px; width: 140px; height: 70px; }
  .card-front .band { height: 15px; }
  .card-person { position: absolute; left: 6px; top: 34px; line-height: 1; }
  .card-person-name { font-size: 6px; letter-spacing: 0.05em; color: var(--ink); text-transform: uppercase; }
  .card-person-role { font-size: 4px; letter-spacing: 0.05em; color: var(--ink); text-transform: uppercase; margin-top: 2px; }
</style>
</head>
<body>

  <div class="piece envelope-back">
    <svg width="341" height="46" viewBox="0 0 341 46" aria-hidden="true">
      <path d="M0 0 H341 L330 38 Q328 45 320 45 H21 Q13 45 11 38 Z" fill="var(--brand-grey)"/>
    </svg>
    <div class="flap-square"></div>
  </div>

  <div class="piece envelope-front">
    <div class="brand" style="left:31px; top:30px;">
      <div class="brand-square" style="width:31px;height:31px;"></div>
      <div class="brand-name" style="font-size:15px;">Kestrel<br>Blinds</div>
    </div>
    <div class="band"></div>
  </div>

  <div class="piece compliments">
    <div class="brand" style="left:30px; top:25px;">
      <div class="brand-square" style="width:29px;height:29px;"></div>
      <div class="brand-name" style="font-size:14px;">Kestrel<br>Blinds</div>
    </div>
    <div class="compliments-note">With Compliments</div>
    <div class="band"></div>
  </div>

  <div class="piece letterhead">
    <div class="brand" style="left:33px; top:32px;">
      <div class="brand-square" style="width:29px;height:29px;"></div>
      <div class="brand-name" style="font-size:14px;">Kestrel<br>Blinds</div>
    </div>
    <div class="band"></div>
  </div>

  <div class="piece folder">
    <div class="brand" style="left:18px; top:22px;">
      <div class="brand-square" style="width:32px;height:32px;"></div>
      <div class="brand-name" style="font-size:15px;">Kestrel<br>Blinds</div>
    </div>
    <div class="band"></div>
    <div class="folder-square"></div>
  </div>

  <svg class="cd-disc" width="190" height="190" viewBox="0 0 190 190" aria-hidden="true">
    <circle cx="95" cy="95" r="94" fill="var(--paper-white)"/>
    <circle cx="105" cy="92" r="19" fill="#d8d8d8"/>
    <circle cx="105" cy="92" r="12" fill="var(--backdrop)"/>
    <rect x="136" y="82" width="30" height="30" fill="var(--accent)"/>
  </svg>

  <div class="piece cd-sleeve">
    <div class="brand" style="left:44px; top:35px; gap:7px;">
      <div class="brand-square" style="width:26px;height:26px;"></div>
      <div class="brand-name" style="font-size:12px;">Kestrel<br>Blinds</div>
    </div>
    <div class="band"></div>
    <div class="sleeve-square"></div>
  </div>

  <div class="piece card-back">
    <div class="card-back-square"></div>
    <div class="card-back-url">www.kestrelblinds.com.au</div>
  </div>

  <div class="piece card-front">
    <div class="brand" style="left:6px; top:7px; gap:4px;">
      <div class="brand-square" style="width:15px;height:15px;"></div>
      <div class="brand-name" style="font-size:7px;">Kestrel<br>Blinds</div>
    </div>
    <div class="card-person">
      <div class="card-person-name">Name Name</div>
      <div class="card-person-role">Position</div>
    </div>
    <div class="band"></div>
  </div>

</body>
</html>
```